MOLVT Study flyer

I need help designing a flyer for a research study that will include brain imaging in adolescents. The info is in the attached document. The study is called the Marrowby Orchard Lantern Vesper Trail (MOLVT) study. Ideally this would be returned as a document that I can edit in the future as we will have several new recruitment phases (different age groups, etc. I also would love to have a logo designed as part of this project, but I recognize that might be a separate design request.

```html
<!DOCTYPE html>
<html lang="en">
<head>
<meta charset="utf-8">
<title>MOLVT Study Flyer</title>
<link rel="stylesheet" href="https://fonts.googleapis.com/css2?family=Bebas+Neue&family=Montserrat:wght@400;500;600;700&display=swap">
<style>
  :root {
    --ink: #111111;
    --headline-blue: #2b6db3;
    --peach: #f2b18b;
    --sky: #0ba3e2;
    --chestnut: #652a06;
    --icon-blue: #2f78c4;
    --icon-peach: #f0b187;
    --white: #ffffff;
    --page-bg: #4a4a4a;
  }
  * { box-sizing: border-box; margin: 0; padding: 0; }
  html, body { width: 727px; height: 1200px; overflow: hidden; background: var(--page-bg); }
  .flyer {
    position: relative; width: 727px; height: 1200px; overflow: hidden;
    background: var(--white); font-family: "Montserrat", sans-serif; color: var(--ink);
  }
  .photo-area {
    position: absolute; left: 0; top: 150px; width: 727px; height: 440px;
    background: linear-gradient(180deg, #ffffff 0%, #e9ecee 22%, #d9dde0 55%, #cfc8c0 100%);
  }
  .backdrop { position: absolute; inset: 0; width: 727px; height: 1200px; }
  .headline { position: absolute; top: 18px; left: 0; width: 100%; text-align: center; }
  .headline-lead {
    font-family: "Bebas Neue", sans-serif; font-size: 54px; line-height: 50px; color: var(--ink);
  }
  .headline-main {
    font-family: "Bebas Neue", sans-serif; font-size: 82px; line-height: 72px; color: var(--headline-blue);
  }
  .headline-sub {
    font-size: 28px; line-height: 28px; font-weight: 500; color: var(--ink); margin-top: -2px;
  }
  .intro {
    position: absolute; left: 34px; top: 568px; width: 345px;
    font-size: 16.5px; line-height: 21px; font-weight: 500; color: var(--ink);
  }
  .section-title {
    position: absolute; left: 34px; top: 756px;
    font-size: 22px; font-weight: 600; color: var(--ink);
  }
  .involve-list { position: absolute; left: 32px; top: 795px; width: 360px; list-style: none; }
  .involve-list li {
    display: flex; align-items: flex-start; gap: 14px; margin-bottom: 14px;
    font-size: 12.5px; line-height: 14.5px; font-weight: 600;
  }
  .icon-badge { flex: 0 0 30px; width: 30px; height: 30px; }
  .eligibility-title {
    position: absolute; left: 400px; top: 560px; width: 320px; text-align: center;
    font-size: 22px; line-height: 25px; font-weight: 600; color: var(--white);
  }
  .eligibility-list { position: absolute; left: 434px; top: 630px; width: 280px; list-style: none; }
  .eligibility-list li {
    display: flex; align-items: flex-start; gap: 12px; margin-bottom: 16px;
    font-size: 12.5px; line-height: 17px; font-weight: 700; color: var(--white);
  }
  .eligibility-list .icon-badge { flex-basis: 30px; }
  .compensation { position: absolute; left: 400px; top: 895px; width: 240px; text-align: center; color: var(--white); }
  .compensation-label { font-family: "Bebas Neue", sans-serif; font-size: 44px; line-height: 40px; margin-top: 4px; }
  .compensation-upto { font-size: 30px; line-height: 26px; font-weight: 700; }
  .compensation-amount { font-size: 60px; line-height: 62px; font-weight: 700; }
  .cta { position: absolute; left: 36px; top: 1094px; color: var(--white); }
  .cta-questions { font-family: "Bebas Neue", sans-serif; font-size: 26px; line-height: 24px; }
  .cta-invite { font-size: 30px; line-height: 40px; font-weight: 400; margin-top: 4px; }
  .contact {
    position: absolute; left: 448px; top: 1166px; display: flex; align-items: center; gap: 8px;
    color: var(--white); font-size: 13.5px; font-weight: 500;
  }
</style>
</head>
<body>
<main class="flyer">
  <div class="photo-area" role="img" aria-label="Photo of a researcher fitting headphones on a young girl beside an MRI scanner while a young man looks on"></div>

  <svg class="backdrop" viewBox="0 0 727 1200" aria-hidden="true">
    <path d="M0 517 C 60 500, 150 495, 230 515 C 300 535, 350 560, 368 585 L 395 1200 L 0 1200 Z" fill="var(--peach)"/>
    <path d="M368 585 C 440 520, 560 500, 727 503 L 727 1200 L 420 1200 C 440 1160, 430 1135, 426 1132 C 380 1080, 380 1040, 395 1009 C 430 930, 450 860, 426 804 C 410 720, 380 650, 368 585 Z" fill="var(--sky)"/>
    <path d="M0 517 C 60 500, 150 495, 230 515 C 300 535, 350 560, 368 585 C 440 520, 560 500, 727 503" fill="none" stroke="var(--white)" stroke-width="5"/>
    <path d="M368 585 C 380 650, 410 720, 426 804 C 450 860, 430 930, 395 1009 C 380 1040, 380 1080, 426 1132 C 450 1150, 480 1150, 495 1146" fill="none" stroke="var(--white)" stroke-width="5"/>
    <path d="M0 1052 C 60 1030, 160 1030, 260 1062 C 340 1090, 400 1140, 495 1146 C 580 1140, 620 1100, 650 1070 C 680 1045, 705 1040, 727 1040 L 727 1200 L 0 1200 Z" fill="var(--chestnut)"/>
  </svg>

  <header class="headline">
    <div class="headline-lead">Are you the parent of</div>
    <div class="headline-main">A child age 10-17?</div>
    <div class="headline-sub">Do they worry or overthink<br>negative emotions?</div>
  </header>

  <p class="intro">Halvern State University researchers are seeking girls age 10-17 for a study about brain activity in emotions and decision-making and how they relate to puberty, anxiety and depression.</p>

  <h2 class="section-title">Study participation involves :</h2>
  <ul class="involve-list">
    <li>
      <svg class="icon-badge" viewBox="0 0 30 30" aria-hidden="true"><circle cx="15" cy="15" r="14" fill="var(--icon-blue)" stroke="var(--white)" stroke-width="1.5"/><circle cx="11" cy="11" r="2.5" fill="none" stroke="#fff" stroke-width="1.3"/><circle cx="19" cy="11" r="2.5" fill="none" stroke="#fff" stroke-width="1.3"/><rect x="7" y="16" width="16" height="6" rx="1.5" fill="none" stroke="#fff" stroke-width="1.3"/></svg>
      <span>One one-hour interview (online or in-person) where your child will discuss their thoughts</span>
    </li>
    <li>
      <svg class="icon-badge" viewBox="0 0 30 30" aria-hidden="true"><circle cx="15" cy="15" r="14" fill="var(--icon-blue)" stroke="var(--white)" stroke-width="1.5"/><rect x="8" y="8" width="14" height="10" rx="1" fill="none" stroke="#fff" stroke-width="1.3"/><line x1="11" y1="11.5" x2="19" y2="11.5" stroke="#fff" stroke-width="1.2"/><line x1="11" y1="14.5" x2="17" y2="14.5" stroke="#fff" stroke-width="1.2"/><line x1="15" y1="18" x2="15" y2="22" stroke="#fff" stroke-width="1.3"/><line x1="11" y1="22" x2="19" y2="22" stroke="#fff" stroke-width="1.3"/></svg>
      <span>Online questionnaires<br>(parent and child)</span>
    </li>
    <li>
      <svg class="icon-badge" viewBox="0 0 30 30" aria-hidden="true"><circle cx="15" cy="15" r="14" fill="var(--icon-blue)" stroke="var(--white)" stroke-width="1.5"/><circle cx="15" cy="14" r="7" fill="none" stroke="#fff" stroke-width="1.4"/><circle cx="15" cy="14" r="3.5" fill="none" stroke="#fff" stroke-width="1.2"/><line x1="8" y1="22" x2="22" y2="22" stroke="#fff" stroke-width="1.4"/></svg>
      <span>One two-hour visit where your child will complete an MRI scan, answer questions about their puberty stage, and have a small hair sample taken to study puberty hormones</span>
    </li>
  </ul>

  <h2 class="eligibility-title">Your child may be<br>eligible if they:</h2>
  <ul class="eligibility-list">
    <li>
      <svg class="icon-badge" viewBox="0 0 30 30" aria-hidden="true"><circle cx="15" cy="15" r="14" fill="var(--icon-peach)" stroke="var(--white)" stroke-width="1.5"/><circle cx="11" cy="11" r="2.5" fill="none" stroke="#5a3a22" stroke-width="1.2"/><circle cx="19" cy="11" r="2.5" fill="none" stroke="#5a3a22" stroke-width="1.2"/><path d="M7 21 q4 -6 8 0 q4 -6 8 0" fill="none" stroke="#5a3a22" stroke-width="1.2"/></svg>
      <span>Are age 10-17</span>
    </li>
    <li>
      <svg class="icon-badge" viewBox="0 0 30 30" aria-hidden="true"><circle cx="15" cy="15" r="14" fill="var(--icon-peach)" stroke="var(--white)" stroke-width="1.5"/><circle cx="15" cy="12" r="5" fill="none" stroke="#5a3a22" stroke-width="1.2"/><path d="M8 23 q7 -8 14 0" fill="none" stroke="#5a3a22" stroke-width="1.2"/></svg>
      <span>Tend to worry or overthink negative thoughts</span>
    </li>
    <li>
      <svg class="icon-badge" viewBox="0 0 30 30" aria-hidden="true"><circle cx="15" cy="15" r="14" fill="var(--icon-peach)" stroke="var(--white)" stroke-width="1.5"/><circle cx="15" cy="14" r="6" fill="none" stroke="#5a3a22" stroke-width="1.2"/><line x1="11" y1="10" x2="19" y2="18" stroke="#5a3a22" stroke-width="1.2"/></svg>
      <span>have not been diagnosed with psychosis, learning problems, or autism Interested in partici-pating? Want more informa-tion? Please contact us!</span>
    </li>
  </ul>

  <section class="compensation">
    <svg width="80" height="76" viewBox="0 0 80 76" aria-hidden="true">
      <path d="M34 6 l12 0 l-4 8 l-4 0 z" fill="#000"/>
      <circle cx="40" cy="36" r="22" fill="#000"/>
      <text x="40" y="45" text-anchor="middle" font-family="Montserrat, sans-serif" font-size="22" font-weight="700" fill="var(--sky)">$</text>
      <path d="M10 60 q20 -6 32 2 l22 -10 q6 0 2 6 l-24 14 l-32 0 z" fill="#000"/>
      <rect x="2" y="56" width="10" height="18" fill="#000"/>
    </svg>
    <div class="compensation-label">Compensation</div>
    <div class="compensation-upto">up to</div>
    <div class="compensation-amount">$140</div>
  </section>

  <section class="cta">
    <div class="cta-questions">Interested in participating?<br>Want more information?</div>
    <div class="cta-invite">Please contact us!</div>
  </section>

  <div class="contact">
    <svg width="18" height="13" viewBox="0 0 18 13" aria-hidden="true"><rect x="0.5" y="0.5" width="17" height="12" fill="#fff"/><path d="M0.5 0.5 L9 7 L17.5 0.5" fill="none" stroke="var(--chestnut)" stroke-width="1.3"/></svg>
    <span>molvtstudy@halvernhealth.org</span>
  </div>
</main>
</body>
</html>
```